Web Design Project

We need a web design for a new company that we started called ZARN CNG. ZARN CNG is a company that will build, own and operate compressed natural gas fueling stations throughout the United States. Our primary customers are Trucking companies and the stations will be built for semi trucks. CNG is better for the environment than diesel fuel, and will save trucking companies loads of money. It is also a domestic product which means that it will create American jobs and help America become energy independent. I have attached a logo that we are using. We dont need to stay with this logo persay, but it is what we have for now. We have a video on Vidlo that shows a bit of what we are doing. just search for ZARN CNG. ZARN CNG is a sister company of Holtmark of Arizona,www.hkqvz.example and a nationwide distributor of TRIVEX FUEL, www.trivexfuel.example. We will need links to these sites. Please make any pictures of trucks Holtmark trucks, and please do not use pictures of cabover trucks.

Target Market(s)

The target market are truck drivers and truckers.

Industry/Entity Type

Environment

Requirements
Must have
• Map showing station locations, a page with industry news, a page with a savings calculator (we can code the calculator) Site should have links to

```html
<!DOCTYPE html>
<html lang="en">
<head>
<meta charset="utf-8">
<title>ZARN CNG — Trucks</title>
<link rel="stylesheet" href="https://fonts.googleapis.com/css2?family=Questrial&family=Roboto+Condensed:wght@400&family=Arimo:wght@400;700&display=swap">
<style>
  :root {
    --page-black: #000;
    --frame-dark: #1b1b1b;
    --nav-top: #9a9a9a;
    --nav-bottom: #4a4a4a;
    --nav-divider: #3a3a3a;
    --text-white: #fff;
    --accent-cyan: #1a9fc7;
    --accent-green: #1f9a4a;
    --heading-grey: #5a5a5a;
    --body-black: #111;
    --thumb-frame: #8b8b8b;
    --panel-white: #fff;
    --footer-top: #1ba7cf;
    --footer-bottom: #0a7fa8;
  }
  * { box-sizing: border-box; margin: 0; padding: 0; }
  html, body { width: 1000px; height: 1200px; overflow: hidden; }
  body {
    position: relative;
    background: linear-gradient(90deg, var(--page-black) 0, var(--frame-dark) 3%, var(--page-black) 6%, var(--page-black) 94%, var(--frame-dark) 97%, var(--page-black) 100%);
    font-family: "Arimo", Arial, sans-serif;
    color: var(--body-black);
  }

  .site-header { position: absolute; left: 0; top: 0; width: 1000px; height: 116px; background: var(--page-black); }
  .brand {
    position: absolute; left: 86px; top: 26px;
    display: flex; align-items: center; gap: 16px;
    font-family: "Questrial", sans-serif; font-size: 66px; line-height: 1;
    color: var(--accent-green); letter-spacing: 1px;
  }
  .brand-mark { width: 26px; height: 26px; border-radius: 50%; background: var(--accent-cyan); }
  .tagline {
    position: absolute; left: 521px; top: 54px;
    font-family: "Roboto Condensed", sans-serif; font-size: 22px;
    color: var(--text-white);
  }

  .main-nav {
    position: absolute; left: 0; top: 116px; width: 1000px; height: 44px;
    background: linear-gradient(var(--nav-top), #777 45%, var(--nav-bottom));
    border-top: 2px solid #c4c4c4;
  }
  .main-nav ul { list-style: none; display: flex; justify-content: center; height: 100%; padding-left: 4px; }
  .main-nav li {
    display: flex; align-items: center; padding: 0 13px;
    border-left: 1px solid var(--nav-divider);
    font-size: 14px; font-weight: 700; color: var(--text-white);
    text-transform: uppercase; letter-spacing: 0.1px;
  }
  .main-nav li:first-child { border-left: none; }
  .main-nav li.is-active { color: var(--accent-cyan); }

  .hero {
    position: absolute; left: 25px; top: 160px; width: 935px; height: 391px;
    background:
      radial-gradient(ellipse at 45% 40%, rgba(190,200,215,0.9) 0%, rgba(120,130,145,0.6) 35%, rgba(20,20,25,0.9) 75%),
      linear-gradient(#b7c1d0 0%, #8d96a4 55%, #2a2a2c 75%, #0b0b0c 100%);
  }

  .content {
    position: absolute; left: 31px; top: 551px; width: 929px; height: 542px;
    background: var(--panel-white);
  }
  .page-title {
    position: absolute; left: 39px; top: 38px;
    font-family: "Questrial", sans-serif; font-weight: 400; font-size: 40px;
    color: var(--heading-grey);
  }
  .truck-list { position: absolute; left: 36px; top: 98px; width: 870px; height: 360px; }
  .truck-card { position: absolute; top: 0; width: 201px; }
  .truck-card:nth-child(1) { left: 0; }
  .truck-card:nth-child(2) { left: 221px; }
  .truck-card:nth-child(3) { left: 440px; }
  .truck-card:nth-child(4) { left: 660px; }
  .truck-photo {
    width: 201px; height: 122px; border: 6px solid var(--thumb-frame);
  }
  .truck-photo span { display: block; width: 100%; height: 100%; }
  .photo-dusk { background: linear-gradient(#a9b7cc, #6a7485 60%, #3a3f48); }
  .photo-field { background: linear-gradient(#3f7fd0, #a9c6e6 50%, #4f8a3a 85%); }
  .photo-lot { background: linear-gradient(#b9cce0, #4b6aa8 50%, #8a8a85); }
  .photo-yard { background: linear-gradient(#c8d4e2, #3a66c4 55%, #9a9a96); }
  .truck-name {
    margin-top: 17px; font-size: 13px; font-weight: 700; color: var(--accent-cyan);
    margin-left: 2px;
  }
  .truck-copy { margin-top: 17px; margin-left: 2px; font-size: 12.6px; line-height: 17.5px; color: var(--body-black); }
  .truck-copy p + p { margin-top: 17.5px; }
  .range-link {
    position: absolute; left: 40px; top: 478px;
    font-family: "Questrial", sans-serif; font-size: 19.5px; color: var(--accent-cyan);
    letter-spacing: 0.3px;
  }

  .site-footer {
    position: absolute; left: 31px; top: 1093px; width: 929px; height: 82px;
    background: linear-gradient(var(--footer-top), var(--footer-bottom));
  }
  .footer-brand {
    position: absolute; left: 46px; top: 20px;
    font-family: "Questrial", sans-serif; font-size: 42px; line-height: 1;
    color: var(--text-white);
  }
  .footer-links {
    position: absolute; right: 35px; top: 23px; text-align: right;
    font-size: 13px; line-height: 21px; color: var(--text-white);
  }
  .footer-links .copyright { font-weight: 700; }
</style>
</head>
<body>
  <header class="site-header">
    <div class="brand"><span>ZARN CNG</span><span class="brand-mark"></span></div>
    <p class="tagline">Helping America become energy independent.</p>
  </header>

  <nav class="main-nav">
    <ul>
      <li>Home</li>
      <li>About Us</li>
      <li class="is-active">Trucks</li>
      <li>Dual Fuel</li>
      <li>Savings Calculator</li>
      <li>Locations</li>
      <li>QLD</li>
      <li>Contact Us</li>
    </ul>
  </nav>

  <div class="hero" role="img" aria-label="Photo of a dark semi truck with a long trailer on an open road under a dusk sky"></div>

  <main class="content">
    <h1 class="page-title">Trucks</h1>
    <section class="truck-list">
      <article class="truck-card">
        <div class="truck-photo"><span class="photo-dusk" role="img" aria-label="Photo of a black semi truck with trailer at dusk"></span></div>
        <h2 class="truck-name">Name of truck</h2>
        <div class="truck-copy">
          <p>Lorem ipsum dolor sit amet, consectetur adipiscing elit. Aenean eu lacus enim.</p>
          <p>In quis tincidunt sem. Praesent egestas rutrum vestibulum. Nulla dapibus, libero at eleifend molestie, elit est aliquam diam, quis adipiscing est nulla et nulla. Aliquam erat volutpat.</p>
        </div>
      </article>
      <article class="truck-card">
        <div class="truck-photo"><span class="photo-field" role="img" aria-label="Photo of a silver semi truck with white trailer by a green field"></span></div>
        <h2 class="truck-name">Name of truck</h2>
        <div class="truck-copy">
          <p>Lorem ipsum dolor sit amet, consectetur adipiscing elit. Aenean eu lacus enim.</p>
          <p>In quis tincidunt sem. Praesent egestas rutrum vestibulum. Nulla dapibus, libero at eleifend molestie, elit est aliquam diam, quis adipiscing est nulla et nulla. Aliquam erat volutpat.</p>
        </div>
      </article>
      <article class="truck-card">
        <div class="truck-photo"><span class="photo-lot" role="img" aria-label="Photo of a blue truck cab seen from the front on a dealer lot"></span></div>
        <h2 class="truck-name">Name of truck</h2>
        <div class="truck-copy">
          <p>Lorem ipsum dolor sit amet, consectetur adipiscing elit. Aenean eu lacus enim.</p>
          <p>In quis tincidunt sem. Praesent egestas rutrum vestibulum. Nulla dapibus, libero at eleifend molestie, elit est aliquam diam, quis adipiscing est nulla et nulla. Aliquam erat volutpat.</p>
        </div>
      </article>
      <article class="truck-card">
        <div class="truck-photo"><span class="photo-yard" role="img" aria-label="Photo of a bright blue truck cab parked in a truck yard"></span></div>
        <h2 class="truck-name">Name of truck</h2>
        <div class="truck-copy">
          <p>Lorem ipsum dolor sit amet, consectetur adipiscing elit. Aenean eu lacus enim.</p>
          <p>In quis tincidunt sem. Praesent egestas rutrum vestibulum. Nulla dapibus, libero at eleifend molestie, elit est aliquam diam, quis adipiscing est nulla et nulla. Aliquam erat volutpat.</p>
        </div>
      </article>
    </section>
    <p class="range-link">View the full range available at www.hkqvz.example</p>
  </main>

  <footer class="site-footer">
    <div class="footer-brand">ZARN CNG</div>
    <div class="footer-links">
      <p>Sitemap | Privacy Policy | Disclaimer | Contact us</p>
      <p class="copyright">© ZARN CNG 2013</p>
    </div>
  </footer>
</body>
</html>
```